Postcard Design

I have a vacation rental business in Burnet, Texas in the Texas Hill Country. I need a one page flyer type handout for use with the local area chambers of commerce.

I have a website - www.quillmeadowlodges.com

I have a business card - that Pressolux did the printing on

Requirements
Must have
• Need to have an arrowhead in the design

Need you to go to the website for some of the information and then the flyer needs to have all the business card information on it too.
Nice to have
• Printing on both sides

```html
<!DOCTYPE html>
<html lang="en">
<head>
<meta charset="utf-8">
<title>Quill Meadow on Lake Sorrel – Postcard</title>
<link rel="stylesheet" href="https://fonts.googleapis.com/css2?family=Cinzel:wght@400;700&family=Raleway:wght@300&family=Oswald:wght@500;600&family=Lato:wght@700&display=swap">
<style>
  :root {
    --lake-blue: #3e5d86;
    --navy: #24395a;
    --ink: #0a0a0a;
    --paper: #ffffff;
    --body-grey: #555555;
    --mist: #e6e6e6;
    --brand-blue: #3e5d86;
  }
  * { box-sizing: border-box; margin: 0; padding: 0; }
  html, body { width: 1200px; height: 900px; overflow: hidden; background: var(--paper); }
  .postcard { position: relative; width: 1200px; height: 900px; overflow: hidden; background: var(--paper); }

  .header { position: absolute; left: 0; top: 0; width: 1200px; height: 380px; }
  .header svg { display: block; }

  .title-block { position: absolute; left: 0; top: 112px; width: 610px; text-align: center; color: var(--paper); }
  .title-name { font-family: "Cinzel", serif; font-weight: 400; font-size: 54px; letter-spacing: 1px; line-height: 1; white-space: nowrap; }
  .title-place { font-family: "Raleway", sans-serif; font-weight: 300; font-size: 44px; letter-spacing: 0.5px; line-height: 1.1; margin-top: 6px; white-space: nowrap; }
  .title-tagline { font-family: "Oswald", sans-serif; font-weight: 500; font-size: 27px; line-height: 1.2; margin-top: 8px; white-space: nowrap; }

  .intro-area { position: absolute; left: 0; top: 380px; width: 1200px; height: 332px;
    background: linear-gradient(180deg, #ffffff 0%, #f2f2f2 55%, var(--mist) 100%); }
  .intro-text { position: absolute; left: 33px; top: 34px; width: 1110px;
    font-family: "Lato", sans-serif; font-weight: 700; font-size: 18.5px; line-height: 30.5px; color: var(--body-grey); }
  .wrap-spacer { float: right; width: 0; height: 120px; }
  .wrap-block { float: right; clear: right; width: 250px; height: 160px; }

  .contact-band { position: absolute; left: 0; top: 712px; width: 1200px; height: 122px; background: var(--ink); }
  .manager { position: absolute; left: 345px; top: 22px; width: 540px; text-align: center; color: var(--paper); }
  .manager-name { font-family: "Cinzel", serif; font-weight: 400; font-size: 25px; letter-spacing: 1px; white-space: nowrap; }
  .manager-email { font-family: "Cinzel", serif; font-size: 15px; letter-spacing: 1px; margin-top: 6px; display: flex; align-items: center; justify-content: center; gap: 6px; white-space: nowrap; }

  .brand-box { position: absolute; left: 33px; top: 662px; width: 295px; height: 148px; background: var(--paper); border-radius: 12px;
    display: flex; flex-direction: column; align-items: center; justify-content: center; gap: 6px; color: var(--brand-blue); }
  .brand-name { font-family: "Cinzel", serif; font-weight: 400; font-size: 27px; line-height: 1.1; text-align: center; }
  .brand-place { font-family: "Cinzel", serif; font-weight: 400; font-size: 17px; }
  .brand-dot { width: 14px; height: 14px; border-radius: 50%; background: var(--brand-blue); margin-top: 4px; }

  .footer-band { position: absolute; left: 0; top: 846px; width: 1200px; height: 54px; }

  .starburst { position: absolute; left: 880px; top: 556px; width: 304px; height: 304px; }
  .burst-contact { position: absolute; left: 880px; top: 556px; width: 304px; height: 304px;
    display: flex; flex-direction: column; align-items: center; justify-content: center; padding-top: 40px; color: var(--lake-blue); }
  .burst-phone { font-family: "Oswald", sans-serif; font-weight: 600; font-size: 27px; display: flex; align-items: center; gap: 7px; white-space: nowrap; }
  .burst-web { font-family: "Oswald", sans-serif; font-weight: 500; font-size: 14px; margin-top: 2px; white-space: nowrap; }
</style>
</head>
<body>
<div class="postcard">

  <div class="header">
    <svg width="1200" height="380" viewBox="0 0 1200 380">
      <defs>
        <linearGradient id="lodgeTones" x1="0" y1="0" x2="0" y2="1">
          <stop offset="0" stop-color="#6f8a4c"/>
          <stop offset="0.35" stop-color="#9a6a55"/>
          <stop offset="0.62" stop-color="#7b4a3a"/>
          <stop offset="0.75" stop-color="#6fae3c"/>
          <stop offset="1" stop-color="#4f8f2a"/>
        </linearGradient>
      </defs>
      <g role="img" aria-label="Photo of the lodge with red railings, shade tree and green lawn">
        <rect x="640" y="0" width="560" height="360" fill="url(#lodgeTones)"/>
      </g>
      <polygon points="0,0 640,0 745,180 640,360 0,360" fill="var(--lake-blue)"/>
      <polygon points="652,0 676,0 781,180 676,360 652,360 757,180" fill="var(--paper)"/>
      <polygon points="684,0 694,0 799,180 694,360 684,360 789,180" fill="var(--navy)"/>
      <rect x="0" y="360" width="1200" height="20" fill="var(--navy)"/>
    </svg>
  </div>

  <div class="title-block">
    <h1 class="title-name">QUILL MEADOW</h1>
    <p class="title-place">ON LAKE SORREL</p>
    <p class="title-tagline">Nearby Attractions, Activities &amp; Links</p>
  </div>

  <section class="intro-area">
    <p class="intro-text"><span class="wrap-spacer"></span><span class="wrap-block"></span>Quill Meadow Cabins on Lake Sorrel offers privacy and seclusion on 20 acres of lakefront property on the uppermost of the Highland Lakes in the beautiful Texas Hill Country. The property is located on RR 4186 on the deep side of Lake Sorrel, surrounded by spectacular fields of bluebonnets and other wild flowers in the spring. The property boasts a main “log cabin” lodge and three additional cabins that are also available for rental based on your group size. privacy and seclusion on 20 acres of lakefront property on the uppermost of the Highland Lakes in the beautiful Texas Hill Country. The property is located on RR 4186 on the deep side of Lake Sorrel, surrounded by spectacular fields of bluebonnets and other wild flowers in the spring.</p>
  </section>

  <div class="contact-band">
    <div class="manager">
      <p class="manager-name">Dana Whitlow Property Manager</p>
      <p class="manager-email">
        <svg width="16" height="16" viewBox="0 0 16 16" aria-hidden="true"><g fill="none" stroke="#fff" stroke-width="1.2"><circle cx="8" cy="8" r="7"/><ellipse cx="8" cy="8" rx="3" ry="7"/><line x1="1" y1="8" x2="15" y2="8"/><line x1="2.5" y1="4.5" x2="13.5" y2="4.5"/><line x1="2.5" y1="11.5" x2="13.5" y2="11.5"/></g></svg>
        INFO@QUILLMEADOWLODGES.COM
      </p>
    </div>
  </div>

  <div class="brand-box">
    <p class="brand-name">Quill Meadow</p>
    <p class="brand-place">on Lake Sorrel</p>
    <span class="brand-dot"></span>
  </div>

  <svg class="footer-band" width="1200" height="54" viewBox="0 0 1200 54">
    <rect x="0" y="0" width="1200" height="54" fill="var(--ink)"/>
    <polygon points="0,0 345,0 365,27 345,54 0,54" fill="var(--lake-blue)"/>
    <polyline points="350,0 372,27 350,54" fill="none" stroke="#fff" stroke-width="5"/>
    <polygon points="940,0 1200,0 1200,54 940,54 960,27" fill="var(--lake-blue)"/>
    <polyline points="925,0 947,27 925,54" fill="none" stroke="#fff" stroke-width="5"/>
  </svg>

  <svg class="starburst" viewBox="-152 -152 304 304" aria-hidden="true">
    <polygon fill="#fff" stroke="#000" stroke-width="7" stroke-linejoin="miter" points="
      145,0 123.9,16.3 140,37.5 115.5,47.8 125.6,72.5 99.2,76.1 102.5,102.5 76.1,99.2 72.5,125.6 47.8,115.5 37.5,140 16.3,123.9 0,145
      -16.3,123.9 -37.5,140 -47.8,115.5 -72.5,125.6 -76.1,99.2 -102.5,102.5 -99.2,76.1 -125.6,72.5 -115.5,47.8 -140,37.5 -123.9,16.3 -145,0
      -123.9,-16.3 -140,-37.5 -115.5,-47.8 -125.6,-72.5 -99.2,-76.1 -102.5,-102.5 -76.1,-99.2 -72.5,-125.6 -47.8,-115.5 -37.5,-140 -16.3,-123.9 0,-145
      16.3,-123.9 37.5,-140 47.8,-115.5 72.5,-125.6 76.1,-99.2 102.5,-102.5 99.2,-76.1 125.6,-72.5 115.5,-47.8 140,-37.5 123.9,-16.3"/>
  </svg>
  <div class="burst-contact">
    <p class="burst-phone">
      <svg width="22" height="22" viewBox="0 0 22 22" aria-hidden="true"><rect width="22" height="22" rx="4" fill="var(--lake-blue)"/><path d="M7 4.5c-1 .5-2 1.5-1.8 3 .5 4 4.5 8.5 8.8 9.6 1.4.4 2.6-.4 3.2-1.4l-2.6-2.3-1.6 1c-1.8-.8-3.4-2.6-4.1-4.4l1.1-1.5z" fill="#fff"/></svg>
      (512) 555-0148
    </p>
    <p class="burst-web">www.quillmeadowlodges.com</p>
  </div>

</div>
</body>
</html>
```